Swimming Pool Service Website needed!!!

Hi Everyone! Thanks for looking at my contest. I PROMISE to provide excellent feedback during this process.

I am starting a new swimming pool business cleaning company in San Diego, California and would like your help in making it similar to one of these two websites that are already functioning.

http://www.brightmeadowhub.example/services-repair.html

http://tryvelmarktide.example/commercial-pool-cleaning.php

I like these two because they are easy to read, classy, sophisticated and have nice pictures of really clean & clear pools.

I really like the blue on white color format.

I do not have a logo, but the name of my company is HARBORLINE POOL SERVICE.

My tag line is: Water so bright, you'll want to dive right in. (does not need to have the quotes around "in"...maybe just italics for this word IN?) You decide for me.

I would like to have a logo designed that incorporates some sort of easy to read letters. I do not want cursive (handwriting) letters. I thought about having a "reflection" of letters (mirror image), but think that this will be hard to read from far away. Maybe you can surprise me and come up with an idea that works using the a mirror image....but I'm not sure. I was leaning toward plain old BLOCK letters as I think it would be easy to read on my truck.

I would like to have 5 pages on my website:
1) Home
2) About Us (Know Your Poolman) / Why Hire Us
3) Services Offered
4) FAQ's
5) Contact

I am looking for a fully-functioning website (coded). Upon selection of the design winner, I am offering to increase the budget/payment by $100-$125 for the coding of all the pages. So anyone looking at participating in this contest, should be willing and able to provide the coding to the webpages that i've requested.

Target Market(s)

Upper middle-class homeowners who have a pool

Industry/Entity Type

Pool Service

Number of Pages Required

5+ page

Font styles to use
Serif

Colors
0455a3
3276b5
85acd3
85cae6
ffffff
33a6d7
0592cd

Requirements
Must have
• The Home page must have this picture highlighted in the top of the page:
• http://www.dunecrestwaterman.example/
• Must have pictures of some high-end pools. Any that you can find on the internet are wonderful.
• Must have a table on the right of the home page that mentions the service areas that we go to:
• • Carmel Valley (92130)
• • Del Mar (92014)
• • Rancho Santa Fe (92067)
• • Solana Beach (92075)
• • Santaluz (92127)
• • Cardiff (92007)
• • Encinitas (92024)
• • Carlsbad (92009, 92008)
• • La Jolla (92037)
• • Pacific Beach (92109)
• • Mira Mesa (92126)
• • Sorrento Valley (92121)
• • Clairemont (92117)
• • Rancho Bernardo (92127, 92128)
• • Rancho Penasquitos (92129)
• • Poway (92064)
Nice to have
• Maybe incorporate some pictures of some kids (or families) playing in pools on the Why Hire Us page?
• I also like the feel of this website, but posting this page just for reference so you can get a feel more of what I like:
• http://www.ferrovaletide.example/
• I like the FAQ's page from this website. I like how you can click on the question and then it pops up with the answer. http://www.quillbrookaquacare.example/pool-spa-fountain-faqs/

```html
<!DOCTYPE html>
<html lang="en">
<head>
<meta charset="utf-8">
<title>Harborline Pool Service</title>
<link href="https://fonts.googleapis.com/css2?family=Roboto:wght@400;500;700&family=Lato:wght@400;700&family=Noto+Serif:ital,wght@1,700&display=swap" rel="stylesheet">
<style>
:root{
  --blue:#33a6d7;
  --blue-dark:#0592cd;
  --ink:#222;
  --text:#3a3a3a;
  --rule:#e3e3e3;
  --footer:#1c1c1c;
  --accent:#d1264f;
}
*{margin:0;padding:0;box-sizing:border-box}
html,body{width:962px;height:1200px;overflow:hidden;background:#fff}
body{position:relative;font-family:"Lato",sans-serif;color:var(--text)}
.site-header{position:absolute;left:0;top:0;width:962px;height:110px}
.brand{position:absolute;left:60px;top:54px;font-family:"Roboto",sans-serif;font-weight:500;color:#1f2a36;text-align:center;line-height:1.2}
.brand-name{font-size:15px;letter-spacing:1.5px}
.brand-sub{font-size:10px;letter-spacing:2.4px}
.call{position:absolute;right:60px;top:28px;font-family:"Roboto",sans-serif;font-size:9px;color:#333;display:flex;align-items:center;gap:3px}
.call strong{color:var(--blue-dark);font-size:13px;font-weight:500}
.main-nav{position:absolute;right:62px;top:61px;display:flex;align-items:center;font-family:"Roboto",sans-serif;font-size:11.5px;font-weight:500;color:#333}
.main-nav a{color:inherit;text-decoration:none}
.main-nav .current{border:2px solid var(--blue);color:var(--blue-dark);padding:4px 12px;margin-right:16px}
.main-nav .sep{margin:0 10px}
.hero{position:absolute;left:0;top:110px;width:962px;height:420px;background:linear-gradient(180deg,#6f96b5 0%,#b8cfdf 22%,#2d6f98 27%,#56a6d6 45%,#3d8fc7 70%,#5aa9dc 100%)}
.hero-prev{position:absolute;left:34px;top:186px;width:44px;height:44px;border-radius:50%;background:rgba(80,90,100,.35)}
.tagline{position:absolute;right:59px;top:283px;text-align:right;font-family:"Roboto",sans-serif;font-weight:500;font-size:33px;color:#111;line-height:1}
.tagline span.line{display:inline-block;background:rgba(255,255,255,.45);padding:4px 8px;margin-bottom:6px}
.tagline em{font-family:"Noto Serif",serif;font-style:italic;color:var(--accent)}
.welcome{position:absolute;left:60px;top:580px;width:546px}
h2{font-family:"Roboto",sans-serif;font-weight:500;font-size:22px;color:var(--ink)}
.welcome p{margin-top:14px;font-size:10px;line-height:18.5px;text-align:justify}
.btn{display:inline-block;margin-top:18px;background:var(--blue);color:#fff;font-size:10px;padding:9px 16px;text-decoration:none}
.divider{position:absolute;left:60px;top:760px;width:546px;border-top:1px solid var(--rule)}
.services{position:absolute;left:60px;top:788px;width:546px}
.arrows{position:absolute;right:0;top:6px;display:flex;gap:2px}
.cards{position:absolute;top:48px;left:0;width:546px;height:260px}
.card{position:absolute;width:160px;text-align:center}
.card .photo{width:113px;height:113px;border-radius:50%;margin:0 auto}
.card h3{margin-top:10px;font-family:"Roboto",sans-serif;font-weight:500;font-size:12.5px;line-height:19px;color:var(--ink)}
.card p{margin-top:6px;font-size:9.5px;line-height:16.5px;text-align:justify;text-align-last:center}
.card a{display:block;margin-top:4px;font-size:9px;color:var(--blue-dark);text-decoration:none}
.areas{position:absolute;left:639px;top:581px;width:265px}
.areas h2{font-size:16.5px}
.area-list{list-style:none;margin-top:10px;border:1px solid var(--rule);padding:6px 13px 4px}
.area-list li{display:flex;align-items:center;gap:8px;font-size:10px;color:#333;height:27.5px;border-bottom:1px solid #ededed;padding-left:7px}
.area-list li:last-child{border-bottom:none}
.site-footer{position:absolute;left:0;top:1124px;width:962px;height:76px;background:var(--footer)}
.copy{position:absolute;left:61px;top:35px;font-size:9.5px;color:#ddd}
.social{position:absolute;right:60px;top:29px;display:flex;gap:4px}
.social span{width:23px;height:23px;border-radius:50%;background:#fff;display:block}
</style>
</head>
<body>
<header class="site-header">
  <div class="brand"><div class="brand-name">HARBORLINE</div><div class="brand-sub">POOL SERVICE</div></div>
  <div class="call">
    <svg width="10" height="10" viewBox="0 0 24 24"><path fill="#333" d="M6.6 10.8a15 15 0 0 0 6.6 6.6l2.2-2.2c.3-.3.7-.4 1-.2 1.1.4 2.3.6 3.6.6.6 0 1 .4 1 1V20c0 .6-.4 1-1 1A17 17 0 0 1 3 4c0-.6.4-1 1-1h3.5c.6 0 1 .4 1 1 0 1.3.2 2.5.6 3.6.1.3 0 .7-.2 1z"/></svg>
    Call Us: <strong>+1800 555 0147</strong>
  </div>
  <nav class="main-nav">
    <a class="current" href="#">Home</a>
    <a href="#">About us</a><span class="sep">|</span>
    <a href="#">Services offered</a><span class="sep">|</span>
    <a href="#">FAQ's</a><span class="sep">|</span>
    <a href="#">Why Hire us</a><span class="sep">|</span>
    <a href="#">Contact</a>
  </nav>
</header>

<section class="hero" role="img" aria-label="Clean tiled swimming pool with steel ladder under a bright sky">
  <div class="hero-prev">
    <svg width="44" height="44" viewBox="0 0 44 44"><path d="M32 10l-6 6 6 6" transform="translate(-6 6)" fill="none" stroke="#fff" stroke-width="2"/></svg>
  </div>
  <div class="tagline">
    <span class="line">Water so bright, you'll want to</span><br>
    <span class="line">dive right <em>in</em>.</span>
  </div>
</section>

<section class="welcome">
  <h2>Welcome to Our Site..</h2>
  <p>Lorem ipsum dolor sit amet, consectetur adipiscing elit, sed do eiusmod tempor incididunt ut labore et dolore magna aliqua. Ut enim ad minim veniam, quis nostrud exercitation ullamco laboris nisi ut aliquip ex ea commodo consequat. Duis aute irure dolor in reprehenderit in voluptate velit esse cillum dolore eu fugiat nulla pariatur. Excepteur sint occaecat cupidatat non proident, sunt in culpa qui officia deserunt mollit anim id est laborum</p>
  <a class="btn" href="#">READ MORE</a>
</section>
<div class="divider"></div>

<section class="services">
  <h2>Our Services</h2>
  <div class="arrows">
    <svg width="10" height="12" viewBox="0 0 10 12"><path d="M7 1L2 6l5 5" fill="none" stroke="#333" stroke-width="2"/></svg>
    <svg width="10" height="12" viewBox="0 0 10 12"><path d="M3 1l5 5-5 5" fill="none" stroke="#bbb" stroke-width="2"/></svg>
  </div>
  <div class="cards">
    <div class="card" style="left:1px">
      <div class="photo" role="img" aria-label="Child swimming in a pool" style="background:radial-gradient(circle,#e9b9a0 0%,#5fb9e2 70%)"></div>
      <h3>Swimming Pool<br>Cleaning</h3>
      <p>Excepteur sint occaecat cupidatat non proident, sunt in culpa qui officia deserunt.</p>
      <a href="#">READ MORE</a>
    </div>
    <div class="card" style="left:193px">
      <div class="photo" role="img" aria-label="Pool ladder over blue water" style="background:linear-gradient(180deg,#2a7fb8,#5cc0ea)"></div>
      <h3>Install and repair<br>lighting</h3>
      <p>Excepteur sint occaecat cupidatat non proident, sunt in culpa qui officia deserunt.</p>
      <a href="#">READ MORE</a>
    </div>
    <div class="card" style="left:383px">
      <div class="photo" role="img" aria-label="Person relaxing on a green float in a pool" style="background:radial-gradient(circle at 40% 70%,#8be04a 0%,#2e9fd4 55%)"></div>
      <h3>New Pool and Spa<br>Start Ups</h3>
      <p>Excepteur sint occaecat cupidatat non proident, sunt in culpa qui officia deserunt.</p>
      <a href="#">READ MORE</a>
    </div>
  </div>
</section>

<aside class="areas">
  <h2>List of areas covered by us</h2>
  <ul class="area-list">
    <li><svg width="8" height="8" viewBox="0 0 8 8"><path d="M1 1l3 3-3 3M4 1l3 3-3 3" fill="none" stroke="#33a6d7" stroke-width="1.3"/></svg>Carmel Valley (92130)</li>
    <li><svg width="8" height="8" viewBox="0 0 8 8"><path d="M1 1l3 3-3 3M4 1l3 3-3 3" fill="none" stroke="#33a6d7" stroke-width="1.3"/></svg>Del Mar (92014)</li>
    <li><svg width="8" height="8" viewBox="0 0 8 8"><path d="M1 1l3 3-3 3M4 1l3 3-3 3" fill="none" stroke="#33a6d7" stroke-width="1.3"/></svg>Rancho Santa Fe (92067)</li>
    <li><svg width="8" height="8" viewBox="0 0 8 8"><path d="M1 1l3 3-3 3M4 1l3 3-3 3" fill="none" stroke="#33a6d7" stroke-width="1.3"/></svg>Solana Beach (92075)</li>
    <li><svg width="8" height="8" viewBox="0 0 8 8"><path d="M1 1l3 3-3 3M4 1l3 3-3 3" fill="none" stroke="#33a6d7" stroke-width="1.3"/></svg>Santaluz (92127)</li>
    <li><svg width="8" height="8" viewBox="0 0 8 8"><path d="M1 1l3 3-3 3M4 1l3 3-3 3" fill="none" stroke="#33a6d7" stroke-width="1.3"/></svg>Cardiff (92007)</li>
    <li><svg width="8" height="8" viewBox="0 0 8 8"><path d="M1 1l3 3-3 3M4 1l3 3-3 3" fill="none" stroke="#33a6d7" stroke-width="1.3"/></svg>Encinitas (92024)</li>
    <li><svg width="8" height="8" viewBox="0 0 8 8"><path d="M1 1l3 3-3 3M4 1l3 3-3 3" fill="none" stroke="#33a6d7" stroke-width="1.3"/></svg>Carlsbad (92009, 92008)</li>
    <li><svg width="8" height="8" viewBox="0 0 8 8"><path d="M1 1l3 3-3 3M4 1l3 3-3 3" fill="none" stroke="#33a6d7" stroke-width="1.3"/></svg>La Jolla (92037)</li>
    <li><svg width="8" height="8" viewBox="0 0 8 8"><path d="M1 1l3 3-3 3M4 1l3 3-3 3" fill="none" stroke="#33a6d7" stroke-width="1.3"/></svg>Pacific Beach (92109)</li>
    <li><svg width="8" height="8" viewBox="0 0 8 8"><path d="M1 1l3 3-3 3M4 1l3 3-3 3" fill="none" stroke="#33a6d7" stroke-width="1.3"/></svg>Mira Mesa (92126)</li>
    <li><svg width="8" height="8" viewBox="0 0 8 8"><path d="M1 1l3 3-3 3M4 1l3 3-3 3" fill="none" stroke="#33a6d7" stroke-width="1.3"/></svg>Sorrento Valley (92121)</li>
    <li><svg width="8" height="8" viewBox="0 0 8 8"><path d="M1 1l3 3-3 3M4 1l3 3-3 3" fill="none" stroke="#33a6d7" stroke-width="1.3"/></svg>Clairemont (92117)</li>
    <li><svg width="8" height="8" viewBox="0 0 8 8"><path d="M1 1l3 3-3 3M4 1l3 3-3 3" fill="none" stroke="#33a6d7" stroke-width="1.3"/></svg>Rancho Bernardo (92127, 92128)</li>
    <li><svg width="8" height="8" viewBox="0 0 8 8"><path d="M1 1l3 3-3 3M4 1l3 3-3 3" fill="none" stroke="#33a6d7" stroke-width="1.3"/></svg>Rancho Penasquitos (92129)</li>
    <li><svg width="8" height="8" viewBox="0 0 8 8"><path d="M1 1l3 3-3 3M4 1l3 3-3 3" fill="none" stroke="#33a6d7" stroke-width="1.3"/></svg>Poway (92064)</li>
  </ul>
</aside>

<footer class="site-footer">
  <div class="copy">Copyright ©2015, Yoursite. All Right Reserved.</div>
  <div class="social"><span></span><span></span><span></span><span></span><span></span></div>
</footer>
</body>
</html>
```